LoftHaven conversion company design.

Hi,

We specialise in attic/roof conversions to create more space. We have a logo design which we are happy with. We would like someone to design a wrap that will be suitable to be transferred onto a 2008 Corvan 300. This is our first car to be wrapped and is what we require a design for.

However, we would like to see a design that can be utilised on a KT Belozan, and 2021 Lundrelle Vantage van. (I understand the design would change to suit but I would like something that will still look similar when they are sat next to one another).

We have a white background on the car so that would need consideration.

We want something that is noticeable but looks professional.

We will also require are contact information on the design:

email: admin@lofthaven-example.com.au
Website: lofthaven-example.com.au
Tel: 1300748216
Social media icons- Snapvelo, Mingleroo, Boardwisp, Quorble

Please let me know if you require any further detail.

```html
<!DOCTYPE html>
<html lang="en">
<head>
<meta charset="utf-8">
<title>LoftHaven – Van Wrap Side Panel</title>
<link rel="stylesheet" href="https://fonts.googleapis.com/css2?family=Poppins:wght@400;500;600&display=swap">
<style>
  :root {
    --bg: #0d0d0d;
    --panel: #f4f5f6;
    --blue: #2a8ce8;
    --blue-deep: #1f6fd6;
    --blue-soft: #4a9ff0;
    --navy: #1c2a38;
    --grey: #8a9199;
    --wood-light: #d9c6a3;
    --wood-dark: #9c7a52;
  }
  * { margin: 0; padding: 0; box-sizing: border-box; }
  html, body { width: 1200px; height: 554px; overflow: hidden; background: var(--bg); }
  .canvas {
    position: relative; width: 1200px; height: 554px;
    font-family: "Poppins", sans-serif; color: var(--navy);
  }
  .wrap-panel {
    position: absolute; left: 40px; top: 40px; width: 1120px; height: 474px;
    background: var(--panel); border-radius: 28px; overflow: hidden;
  }
  .wrap-graphics { position: absolute; inset: 0; width: 1120px; height: 474px; }

  .contact-block {
    position: absolute; right: 620px; top: 228px;
    text-align: right; display: flex; flex-direction: column; align-items: flex-end; gap: 6px;
  }
  .social-row { display: flex; gap: 12px; margin-bottom: 18px; }
  .social-name { font-size: 13px; font-weight: 600; color: var(--blue); }
  .contact-line {
    display: flex; align-items: center; gap: 8px;
    font-size: 14px; font-weight: 600; color: var(--navy);
  }
  .contact-line svg { width: 14px; height: 14px; flex: none; }
  .contact-line.phone { font-size: 23px; color: var(--blue); margin-top: 2px; }
  .contact-line.phone svg { width: 16px; height: 16px; }

  .brand-block {
    position: absolute; left: 546px; top: 250px; width: 300px;
    display: flex; flex-direction: column; align-items: center;
  }
  .brand-name {
    font-size: 54px; font-weight: 600; color: var(--blue);
    letter-spacing: 0.5px; line-height: 1;
  }
  .brand-tagline { margin-top: 14px; font-size: 15px; font-weight: 500; color: var(--navy); }
  .brand-rule { margin-top: 8px; width: 104px; height: 3px; background: var(--blue); }
</style>
</head>
<body>
<div class="canvas">
  <div class="wrap-panel">
    <svg class="wrap-graphics" viewBox="0 0 1120 474" aria-hidden="false">
      <defs>
        <linearGradient id="atticTones" x1="0" y1="0" x2="1" y2="1">
          <stop offset="0" stop-color="var(--wood-light)"/>
          <stop offset="0.6" stop-color="#c8ad84"/>
          <stop offset="1" stop-color="#e8e3d8"/>
        </linearGradient>
      </defs>
      <!-- blue diamond band -->
      <polygon points="575,62 690,22 760,22 640,110" fill="var(--blue)"/>
      <polygon points="600,100 700,60 770,95 660,140" fill="var(--blue-deep)"/>
      <polygon points="575,160 700,105 760,150 680,190" fill="var(--blue)"/>
      <polygon points="700,195 1120,160 1120,240 950,315" fill="var(--blue)"/>
      <polygon points="760,235 1120,205 1120,290 960,330" fill="var(--blue-soft)" opacity="0.7"/>
      <!-- interior photo area -->
      <polygon role="img" aria-label="Photo of a finished attic conversion with timber ceiling beams and a pendant light"
               points="644,122 750,42 1070,42 1090,140 920,230 820,205"
               fill="url(#atticTones)"/>
    </svg>

    <div class="contact-block">
      <div class="social-row">
        <span class="social-name">Mingleroo</span>
        <span class="social-name">Snapvelo</span>
        <span class="social-name">Quorble</span>
        <span class="social-name">Boardwisp</span>
      </div>
      <div class="contact-line">admin@lofthaven-example.com.au
        <svg viewBox="0 0 16 16"><rect x="1" y="3" width="14" height="10" rx="1" fill="none" stroke="var(--grey)" stroke-width="1.5"/><path d="M1.5 3.5 8 9l6.5-5.5" fill="none" stroke="var(--grey)" stroke-width="1.5"/></svg>
      </div>
      <div class="contact-line">Website: lofthaven-example.com.au
        <svg viewBox="0 0 16 16"><circle cx="8" cy="8" r="6.5" fill="none" stroke="var(--grey)" stroke-width="1.4"/><ellipse cx="8" cy="8" rx="3" ry="6.5" fill="none" stroke="var(--grey)" stroke-width="1.2"/><path d="M1.5 8h13" stroke="var(--grey)" stroke-width="1.2"/></svg>
      </div>
      <div class="contact-line phone">Tel: 1300748216
        <svg viewBox="0 0 16 16"><path d="M4 1.5 6.5 4 5 6c1 2 3 4 5 5l2-1.5 2.5 2.5-2 2.5C7 14 2 9 1.5 3.5Z" fill="var(--grey)"/></svg>
      </div>
    </div>

    <div class="brand-block">
      <div class="brand-name">LoftHaven</div>
      <div class="brand-tagline">Storage • Skylights • Conversions</div>
      <div class="brand-rule"></div>
    </div>
  </div>
</div>
</body>
</html>
```